Business Card Design Project

Hi Designers, this project is currently on hold until the Logo is completed:
Please submit to the Logo project here:
http://work.pitchvault.example/brief.aspx?id=413907

Once logo is completed, it will be attached to this project for you to create business cards with show logo, company name and address

Maren T R Quillby

Osric's Tiny Grey Heron Co.
Fernbrook
Nether Coombsby
North Devon EX91 4TZ

Tel: 01809 417356
Mobile: 07900 263818
email: maren@tiny-grey-heron.example.co.uk

Project Deadline Extended
Reason: Sorry everyone, we have had a sick ewe and I am now behind with this one and need to extend the deadline. Best wishes Maren

The designer who wins the logo brief will be asked to design the business card. Many thanks Maren

Project Deadline Extended
Reason: Sorry everyone, just a chaotic time of year with animals. Need to extend the deadline again..... as I just haven't had enough time to take a good look.... Thank you for your understanding. Maren

Project Deadline Extended
Reason: Sorry everyone It is our busiest time of year with animals and just no time to spend going through such great designs. I will have to extend the deadline again and hopefully have some news very soon. Wishing you all a very happy Christmas and a happy and healthy new year. Maren & Osric

High end market
Boutique restaurants for meat (it's not commercial lamb it's a slow matured quality meat more like venison/beef) expensive - specialized market

High End shoot clothing / wool / sheepskin rugs
Quality products

Business

• based on the logo - (which Pitch Vault has just been asked to do)
possibly based on a simplified picture of a Hebridean Ram (shows it's a Hebridean by it's horns as opposed to other black sheep!!)

```html
<!DOCTYPE html>
<html lang="en">
<head>
<meta charset="utf-8">
<title>Osric's Tiny Grey Heron Co. — Business Card</title>
<link href="https://fonts.googleapis.com/css2?family=Cinzel:wght@400;700&display=swap" rel="stylesheet">
<style>
  :root {
    --backdrop: #e6e6e6;
    --paper: #ffffff;
    --ink: #2c3131;
    --ink-soft: #3a3f3f;
    --slate: #2a2e2e;
    --slate-deep: #1f2323;
    --on-slate: #ffffff;
  }
  * { margin: 0; padding: 0; box-sizing: border-box; }
  html, body {
    width: 1200px; height: 720px; overflow: hidden;
    background: var(--backdrop);
    font-family: "Cinzel", serif;
  }
  .card {
    position: absolute; top: 242px;
    width: 420px; height: 239px; overflow: hidden;
  }
  .card--front { left: 147px; background: var(--paper); color: var(--ink); }
  .card--back {
    left: 634px;
    background: linear-gradient(180deg, var(--slate) 0%, var(--slate-deep) 100%);
    color: var(--on-slate);
  }
  .emblem-area { position: absolute; top: 0; left: 0; }

  .brand { position: absolute; display: flex; align-items: center; }
  .brand__mark { border-radius: 50%; flex: none; }
  .brand__name { font-weight: 400; font-size: 12px; line-height: 1.2; letter-spacing: 0.3px; }

  .brand--front { left: 25px; top: 22px; gap: 9px; }
  .brand--front .brand__mark { width: 26px; height: 26px; background: var(--ink); }

  .brand--back {
    left: 195px; top: 62px; width: 200px;
    flex-direction: column; gap: 14px; text-align: center;
  }
  .brand--back .brand__mark { width: 60px; height: 60px; background: var(--on-slate); }
  .brand--back .brand__name { font-size: 13px; }

  .contact { position: absolute; left: 25px; top: 84px; font-size: 10px; line-height: 12px; }
  .contact__name { font-size: 13px; font-weight: 700; line-height: 15px; }
  .contact__role { margin-bottom: 12px; }
  .contact__address { margin-bottom: 13px; }
  .contact__list { list-style: none; }
  .contact__list li { display: flex; align-items: center; gap: 6px; }
  .contact__list svg { width: 9px; height: 9px; fill: var(--ink-soft); flex: none; }
</style>
</head>
<body>

<section class="card card--front" aria-label="Card front">
  <svg class="emblem-area" width="420" height="239" role="img" aria-label="Large brand emblem decoration">
    <circle cx="445" cy="118" r="144" fill="var(--ink)"/>
  </svg>

  <div class="brand brand--front">
    <span class="brand__mark"></span>
    <span class="brand__name">Osric's Tiny Grey Heron Co.</span>
  </div>

  <div class="contact">
    <p class="contact__name">Maren T R Quillby</p>
    <p class="contact__role">Founder &amp; CEO</p>
    <p class="contact__address">Fernbrook<br>Nether Coombsby<br>North Devon EX91 4TZ</p>
    <ul class="contact__list">
      <li><svg viewBox="0 0 10 10"><path d="M1 3c0-1 1-2 4-2s4 1 4 2v1H7V3H3v1H1zM2 5h6l1 4H1z"/></svg>01809 417356</li>
      <li><svg viewBox="0 0 10 10"><path d="M3 0h4a1 1 0 0 1 1 1v8a1 1 0 0 1-1 1H3a1 1 0 0 1-1-1V1a1 1 0 0 1 1-1zm0 1.5v6h4v-6z"/></svg>07900 263818</li>
      <li><svg viewBox="0 0 10 10"><path d="M0 2h10v6H0zm1 1 4 3 4-3z" fill-rule="evenodd"/></svg>maren@tiny-grey-heron.example.co.uk</li>
      <li><svg viewBox="0 0 10 10"><path d="M0 1h10v6H6v1h1v1H3V8h1V7H0zm1 1v4h8V2z" fill-rule="evenodd"/></svg>www.tiny-grey-heron.example.co.uk</li>
    </ul>
  </div>
</section>

<section class="card card--back" aria-label="Card back">
  <svg class="emblem-area" width="420" height="239" role="img" aria-label="Large brand emblem decoration">
    <circle cx="-26" cy="118" r="144" fill="var(--on-slate)"/>
  </svg>

  <div class="brand brand--back">
    <span class="brand__mark"></span>
    <span class="brand__name">Osric's Tiny Grey Heron Co.</span>
  </div>
</section>

</body>
</html>
```